Hi we have a company called Brenlock Protection Services and are looking for a new design we are wanting flames as the last card was great with the whole background flames but you cant really see the services offered, phone, names etc.

We need something more upmarket and professional and only have a small budget

We need the words Brenlock Protection Services, Martin Pevelle MAQSrT - Fire Safety Consultant, Phone No 0492365140 address : PO Box 8362 TWRL 4183 ABN 71836205947, NRTW Lic.5742816 Email martin@brenlockgroup.com.au

Industry/Entity Type

Fire Safety

Font styles to use
Sans Serif

Colors
ec2027
ffc214

```html
<!DOCTYPE html>
<html lang="en">
<head>
<meta charset="utf-8">
<title>Brenlock Protection Services – Business Card</title>
<link rel="stylesheet" href="https://fonts.googleapis.com/css2?family=Jost:wght@400;500;600&display=swap">
<style>
  :root {
    --backdrop: #0d0119;
    --card: #ececec;
    --ink: #111111;
    --accent: #ffc214;
    --flame-red: #ec2027;
  }
  * { margin: 0; padding: 0; box-sizing: border-box; }
  html, body {
    width: 1200px;
    height: 800px;
    overflow: hidden;
    background: var(--backdrop);
  }
  .canvas {
    position: relative;
    width: 1200px;
    height: 800px;
    display: flex;
    align-items: center;
    justify-content: center;
    font-family: "Jost", "Helvetica Neue", Arial, sans-serif;
    color: var(--ink);
  }
  .business-card {
    position: relative;
    width: 1000px;
    height: 570px;
    background: var(--card);
  }
  .company-name {
    position: absolute;
    left: 53px;
    top: 62px;
    font-size: 30px;
    font-weight: 600;
    letter-spacing: 0.5px;
    text-transform: uppercase;
  }
  .person {
    position: absolute;
    left: 52px;
    top: 375px;
  }
  .person-name {
    font-size: 29px;
    font-weight: 500;
    line-height: 1.1;
  }
  .person-role {
    font-size: 16px;
    font-weight: 400;
    margin-top: 4px;
  }
  .divider {
    position: absolute;
    left: 458px;
    top: 318px;
    width: 2px;
    height: 190px;
    background: var(--accent);
  }
  .contact-list {
    position: absolute;
    left: 514px;
    top: 340px;
    list-style: none;
  }
  .contact-item {
    display: flex;
    align-items: center;
    height: 34px;
    font-size: 20px;
    font-weight: 400;
  }
  .contact-icon {
    width: 19px;
    height: 19px;
    margin-right: 22px;
    flex: none;
  }
</style>
</head>
<body>
<div class="canvas">
  <section class="business-card">
    <h1 class="company-name">Brenlock Protection Services</h1>

    <div class="person">
      <p class="person-name">Martin Pevelle MAQSrT</p>
      <p class="person-role">Fire Safety Consultant</p>
    </div>

    <div class="divider"></div>

    <ul class="contact-list">
      <li class="contact-item">
        <svg class="contact-icon" viewBox="0 0 20 20" aria-hidden="true">
          <rect width="20" height="20" fill="var(--accent)"/>
          <path d="M4 9.5c0-2 3-3.2 6-3.2s6 1.2 6 3.2l-2.4 1-1-1.6V8.2c-1.7-.5-3.5-.5-5.2 0v.7l-1 1.6z" fill="var(--ink)"/>
        </svg>
        0492365140
      </li>
      <li class="contact-item">
        <svg class="contact-icon" viewBox="0 0 20 20" aria-hidden="true">
          <rect width="20" height="20" fill="var(--accent)"/>
          <rect x="4" y="6" width="12" height="8.5" fill="var(--ink)"/>
          <path d="M4 6l6 4.5L16 6" fill="none" stroke="var(--accent)" stroke-width="1.2"/>
        </svg>
        martin@brenlockgroup.com.au
      </li>
      <li class="contact-item">
        <svg class="contact-icon" viewBox="0 0 20 20" aria-hidden="true">
          <rect width="20" height="20" fill="var(--accent)"/>
          <path d="M10 3.5a4.5 4.5 0 0 0-4.5 4.5c0 3.4 4.5 8.5 4.5 8.5s4.5-5.1 4.5-8.5A4.5 4.5 0 0 0 10 3.5z" fill="var(--ink)"/>
          <circle cx="10" cy="8" r="1.7" fill="var(--accent)"/>
        </svg>
        PO Box 8362 TWRL 4183
      </li>
      <li class="contact-item">
        <svg class="contact-icon" viewBox="0 0 20 20" aria-hidden="true">
          <rect width="20" height="20" fill="var(--accent)"/>
          <circle cx="10" cy="10" r="6.5" fill="var(--ink)"/>
          <circle cx="10.3" cy="6.9" r="1" fill="var(--accent)"/>
          <path d="M10.6 9v4.6M9.3 9.2h1.3" stroke="var(--accent)" stroke-width="1.5" fill="none"/>
        </svg>
        ABN 71836205947, NRTW Lic.5742816
      </li>
    </ul>
  </section>
</div>
</body>
</html>
```